Holt & Partners Property Management

I want 4 different cards so that i can mail to my farm once per quarter. I want to go back to a 5X8 card or smaller. I am attaching an example of what we did in the past. I would like the new cards start with the following:
1. Tired of dealing with tenant problems at 6:00 on a Friday Night?
2. Would you like to take you next vacation worry free?
3. Are your tenants paying below market rents?
4. Do your tenant leases fully protect you?
I would like to have one of these "hooks" to lead off each card with a brief explanation of the services we provide. Back of the card can be similar to the one I attached.

Target Market(s)

Income Property Owners that might be in need of a property management company.

Font styles to use
Serif

Requirements
Must have
• 4 separate cards that i can email out each quarter.
• Each card must have a "hook" or "call to action"
Nice to have
• Less verbiage and some catchy graphics or photo
• If you have an idea for catchier calls to action, feel free to submit.
Should not have
• Too many words. The postcard I uploaded has way too much verbiage.

```html
<!DOCTYPE html>
<html lang="en">
<head>
<meta charset="utf-8">
<title>Holt &amp; Partners Property Management – Postcard</title>
<link href="https://fonts.googleapis.com/css2?family=Lato:wght@400;700&family=Roboto+Condensed:wght@700&family=Source+Sans+3:wght@400;600;700&display=swap" rel="stylesheet">
<style>
  :root{
    --bg:#e6e4e1;
    --ink:#3b3b3d;
    --band:#525254;
    --tan:#b99b65;
    --tan-light:#d6c4a4;
    --star:#9c8f80;
    --panel:#f1f1f1;
    --paper:#ffffff;
    --rule:#c9c9c9;
  }
  *{margin:0;padding:0;box-sizing:border-box}
  html,body{width:1009px;height:1200px;overflow:hidden;background:var(--bg)}
  body{position:relative;font-family:"Source Sans 3",sans-serif;color:var(--ink)}

  .card{position:absolute;left:125px;width:776px;height:485px;background:var(--paper);
        box-shadow:0 4px 12px rgba(0,0,0,.25);overflow:hidden}
  .card--front{top:81px}
  .card--back{top:624px}

  .shapes,.photo{position:absolute;inset:0;width:776px;height:485px}

  .brand{position:absolute;left:34px;top:24px;font-family:"Lato",sans-serif;color:var(--ink)}
  .brand__name{font-weight:400;font-size:42px;line-height:33px;letter-spacing:1.5px;text-transform:uppercase}
  .brand__stars{margin-top:8px;font-size:15px;letter-spacing:17px;color:var(--star)}
  .brand__tag{margin-top:0;font-family:"Source Sans 3",sans-serif;font-weight:600;font-size:13.5px;letter-spacing:1.6px}

  .hooks{position:absolute;left:32px;top:160px;list-style:none;color:#fff;font-size:18px;line-height:21px}
  .hooks li{position:relative;padding-left:27px;margin-bottom:10px;white-space:nowrap}
  .hooks svg{position:absolute;left:0;top:2px;width:20px;height:20px}

  .cta{position:absolute;left:33px;font-family:"Roboto Condensed",sans-serif;font-weight:700;font-size:23.5px;letter-spacing:.2px;white-space:nowrap}
  .card--front .cta{top:377px;color:var(--ink)}
  .card--back .cta{top:376px;color:#fff}
  .phone{position:absolute;left:0;top:411px;width:318px;height:42px;background:var(--tan);
         clip-path:polygon(0 0,311px 0,318px 42px,0 42px);color:#fff;
         font-weight:700;font-size:34px;letter-spacing:3px;line-height:42px;padding-left:72px;white-space:nowrap}
  .phone svg{position:absolute;left:31px;top:7px;width:29px;height:29px}
  .web{position:absolute;left:32px;top:455px;font-weight:600;font-size:17px;white-space:nowrap}
  .card--front .web{color:var(--ink)}
  .card--back .web{color:#fff}

  .quote{position:absolute;left:28px;top:166px;width:348px;color:#fff;font-size:12.6px;line-height:14.9px;text-align:justify}
  .quote__mark{font-family:"Lato",sans-serif;font-weight:700;font-size:46px;line-height:0;vertical-align:-16px;margin-right:4px}

  .address{position:absolute;left:454px;top:31px;font-size:12.5px;line-height:15.5px;color:#555;font-style:normal}
  .stamp{position:absolute;left:658px;top:20px;width:97px;height:65px;border:1px solid var(--rule)}
  .lines{position:absolute;left:454px;width:300px;height:1px;background:var(--rule)}
  .lines--1{top:182px}.lines--2{top:223px}.lines--3{top:264px}.lines--4{top:305px}
</style>
</head>
<body>

<!-- FRONT -->
<section class="card card--front">
  <svg class="shapes" viewBox="0 0 776 485">
    <rect x="0" y="149" width="776" height="211" fill="var(--band)"/>
    <polygon points="451,0 776,0 776,485 451,485 320,256" fill="var(--tan-light)"/>
    <polygon points="479,0 776,0 776,485 475,485 346,256" fill="var(--paper)"/>
  </svg>
  <svg class="photo" viewBox="0 0 776 485" role="img" aria-label="Photo: smiling property manager in a navy suit holding out house keys and a small model house">
    <defs>
      <linearGradient id="photoTone" x1="0" y1="0" x2="1" y2="1">
        <stop offset="0" stop-color="#e9ecef"/>
        <stop offset=".55" stop-color="#c3cbd4"/>
        <stop offset="1" stop-color="#3a4556"/>
      </linearGradient>
    </defs>
    <polygon points="507,0 776,0 776,485 480,485 367,256" fill="url(#photoTone)"/>
  </svg>

  <div class="brand">
    <div class="brand__name">Holt &amp;<br>Partners</div>
    <div class="brand__stars">★★★★★</div>
    <div class="brand__tag">PROPERTY MANAGEMENT</div>
  </div>

  <ul class="hooks">
    <li><svg viewBox="0 0 20 20"><circle cx="10" cy="10" r="8.5" fill="none" stroke="var(--tan)" stroke-width="1.6"/><path d="M5.5 9.5l3.3 3.3 6-6.5" fill="none" stroke="var(--tan)" stroke-width="1.8"/></svg>Tired of dealing with tenant problems<br>at 6:00 on a Friday Night?</li>
    <li><svg viewBox="0 0 20 20"><circle cx="10" cy="10" r="8.5" fill="none" stroke="var(--tan)" stroke-width="1.6"/><path d="M5.5 9.5l3.3 3.3 6-6.5" fill="none" stroke="var(--tan)" stroke-width="1.8"/></svg>Would you like to take you next<br>vacation worry free?</li>
    <li><svg viewBox="0 0 20 20"><circle cx="10" cy="10" r="8.5" fill="none" stroke="var(--tan)" stroke-width="1.6"/><path d="M5.5 9.5l3.3 3.3 6-6.5" fill="none" stroke="var(--tan)" stroke-width="1.8"/></svg>Are your tenants paying below<br>market rents?</li>
    <li><svg viewBox="0 0 20 20"><circle cx="10" cy="10" r="8.5" fill="none" stroke="var(--tan)" stroke-width="1.6"/><path d="M5.5 9.5l3.3 3.3 6-6.5" fill="none" stroke="var(--tan)" stroke-width="1.8"/></svg>Do your tenant leases fully protect you?</li>
  </ul>

  <div class="cta">CALL TODAY FOR YOUR FREE QUOTE</div>
  <div class="phone"><svg viewBox="0 0 30 30"><circle cx="15" cy="15" r="13" fill="none" stroke="#fff" stroke-width="2.2"/><path d="M10.5 8.5c1-.8 1.8-.6 2.3.3l1 2c.4.8.2 1.4-.4 1.9l-.8.6c.6 1.6 1.9 3 3.5 3.7l.6-.8c.5-.6 1.1-.8 1.900-.4l2 1c.9.5 1.1 1.3.3 2.3-1.3 1.5-3 1.7-5 .6-2.6-1.4-4.6-3.5-5.8-6.1-.9-2-.7-3.8.4-5.100z" fill="#fff"/></svg>555-014-2290</div>
  <div class="web">holtpartnersproperty.com</div>
</section>

<!-- BACK -->
<section class="card card--back">
  <svg class="shapes" viewBox="0 0 776 485">
    <polygon points="0,0 354,0 419,485 0,485" fill="var(--panel)"/>
    <polygon points="0,147 373,147 401,360 0,360" fill="var(--tan)"/>
    <polygon points="0,360 401,360 419,485 0,485" fill="var(--band)"/>
  </svg>

  <div class="brand">
    <div class="brand__name">Holt &amp;<br>Partners</div>
    <div class="brand__stars">★★★★★</div>
    <div class="brand__tag">PROPERTY MANAGEMENT</div>
  </div>

  <p class="quote"><span class="quote__mark">“</span>We have had Holt &amp; Partners manage our property since 2009. Since that time we have been very pleased with their services. Phone calls or situations are addressed on a timely basis. It really gives us peace of mind knowing that Mark Holt and his company are taking good care of our property. Also, we recently, sold and closed escrow on another property in the North Shore. Mark handled everything to perfection. We would highly recommend Mark Holt and his company to others for any real estate needs. We will be using Mark in the future. He makes it all so easy.<br>- FROM Eleanor R.</p>

  <div class="cta">CALL TODAY FOR YOUR FREE QUOTE</div>
  <div class="phone"><svg viewBox="0 0 30 30"><circle cx="15" cy="15" r="13" fill="none" stroke="#fff" stroke-width="2.2"/><path d="M10.5 8.5c1-.8 1.8-.6 2.3.3l1 2c.4.8.2 1.4-.4 1.9l-.8.6c.6 1.6 1.9 3 3.5 3.7l.6-.8c.5-.6 1.1-.8 1.9-.4l2 1c.9.5 1.1 1.3.3 2.3-1.3 1.5-3 1.7-5 .6-2.6-1.4-4.6-3.5-5.8-6.1-.9-2-.7-3.8.4-5.1z" fill="#fff"/></svg>555-014-2290</div>
  <div class="web">holtpartnersproperty.com</div>

  <address class="address">410 Harbor View Lane,<br>Suite 2 Bayside Estates,<br>CA 90000</address>
  <div class="stamp"></div>
  <div class="lines lines--1"></div>
  <div class="lines lines--2"></div>
  <div class="lines lines--3"></div>
  <div class="lines lines--4"></div>
</section>

</body>
</html>
```